Harbor Crew Biz Cards

looking for a new catchy business card where my cell number is very prominent:
My pic and logo are attached. My whole picture isn't necessary if it makes more sense to crop it.

Info needed:

(Big) Marcus Pellow
(Medium) Real Estate Professional
(Medium) Buyer/Seller Specialist
(Big) Call/Text 410-738-2914
(small) Marcuspell@quillbox.com
(small) www.harborcrewlists.com

(very small)
The Harbor Crew
at Keystead Real Estate
2457 W Tanbrook Rd, Bel Air, MD 21014
833-555-2690

```html
<!DOCTYPE html>
<html lang="en">
<head>
<meta charset="utf-8">
<title>Harbor Crew Business Cards</title>
<link href="https://fonts.googleapis.com/css2?family=Crimson+Pro:wght@400;600;700&display=swap" rel="stylesheet">
<style>
  :root {
    --backdrop: #d9d9db;
    --card: #f7f7f7;
    --navy: #1f3359;
    --ink-grey: #5f5f5f;
    --wreath-grey: #9a9a9a;
    --rule: #2c416b;
  }
  * { box-sizing: border-box; margin: 0; padding: 0; }
  html, body {
    width: 1200px; height: 900px; overflow: hidden;
    background: var(--backdrop);
    font-family: "Crimson Pro", Georgia, serif;
  }
  .card {
    position: absolute; left: 320px; width: 560px; height: 320px;
    background: var(--card); border-radius: 30px;
    box-shadow: 0 10px 24px rgba(0,0,0,.18);
    text-align: center; color: var(--ink-grey);
  }
  .card--front { top: 90px; }
  .card--back { top: 490px; }

  .brand-emblem {
    width: 110px; height: 90px; margin: 34px auto 0;
    border-radius: 50%;
    background: radial-gradient(circle, var(--card) 48%, var(--wreath-grey) 50%, #bdbdbd 72%, var(--card) 74%);
  }
  .brand-name {
    margin-top: 14px; font-size: 40px; font-weight: 600;
    color: var(--navy); letter-spacing: 1px; line-height: 1;
  }
  .brand-office {
    margin-top: 8px; font-size: 13px; letter-spacing: 3px; text-transform: uppercase;
    color: var(--navy);
  }
  .office-phone { margin-top: 20px; font-size: 19px; }
  .office-address { margin-top: 4px; font-size: 19px; }

  .portrait {
    width: 150px; height: 150px; margin: 22px auto 0; border-radius: 50%;
    background: radial-gradient(circle, #d7d9de 0 58%, var(--wreath-grey) 60% 68%, #c4c4c4 70% 74%, var(--card) 76%);
  }
  .agent-name {
    display: flex; align-items: center; gap: 10px;
    margin: 4px 70px 0; font-size: 27px; font-weight: 700; color: var(--navy);
  }
  .agent-name::before, .agent-name::after {
    content: ""; flex: 1; height: 1.5px; background: var(--rule);
  }
  .agent-role { font-size: 17px; margin-top: 0; }
  .agent-mobile { margin-top: 8px; font-size: 25px; font-weight: 700; color: var(--navy); }
  .agent-links { margin-top: 2px; font-size: 17px; }
</style>
</head>
<body>
  <section class="card card--front">
    <div class="brand-emblem" role="img" aria-label="Grey laurel wreath emblem"></div>
    <div class="brand-name">The Harbor Crew</div>
    <div class="brand-office">at Keystead Real Estate</div>
    <p class="office-phone">T. 833-555-2690</p>
    <p class="office-address">2457 W Tanbrook Rd, Bel Air, MD 21014</p>
  </section>

  <section class="card card--back">
    <div class="portrait" role="img" aria-label="Agent portrait in a suit framed by a grey laurel wreath"></div>
    <h1 class="agent-name">Marcus Pellow</h1>
    <p class="agent-role">Real Estate Professional | Buyer/Seller Specialist</p>
    <p class="agent-mobile">M. 410-738-2914</p>
    <p class="agent-links">Marcuspell@quillbox.com | www.harborcrewlists.com</p>
  </section>
</body>
</html>
```